Business cards

Dog breeder selling very high end expensive pets so design must be modern, simple (with the focus being on the photos) and upscale. Would like a full photo on each side of the card with text as an accent more then as the focus.
I would like the name of the business to be large and bold (possibly modern cursive font) and centered preferably but am open to other options
Need the French bulldogs on the front if the card if not both. I was thinking of one full photo on each side but as long as the French Bulldogs are the focus I'm open to all options. The French bulldogs are the ones in the photo with three puppies pictured
Info needed on the card:
Merrywell Kennels
www.merrywellkennels-example.com
themerrywellkennel@examplemail.com
(555) 417-2983
On the back:
Quality pets and champion show dogs

```html
<!DOCTYPE html>
<html lang="en">
<head>
<meta charset="utf-8">
<title>Merrywell Kennels – Business Cards</title>
<link href="https://fonts.googleapis.com/css2?family=Lato:ital,wght@0,400;0,700;1,700&display=swap" rel="stylesheet">
<style>
  :root {
    --bg: #ece8e3;
    --taupe: #c6bcb1;
    --taupe-text: #c2b4a6;
    --white: #ffffff;
    --ink: #3a3632;
    --ink-soft: #4a4541;
  }
  * { box-sizing: border-box; margin: 0; padding: 0; }
  html, body { width: 1200px; height: 1019px; overflow: hidden; }
  body {
    background: var(--bg);
    font-family: 'Lato', sans-serif;
    display: flex;
    flex-direction: column;
    align-items: center;
    justify-content: center;
    gap: 70px;
  }
  .card {
    width: 620px;
    height: 354px;
    background: var(--taupe);
    box-shadow: 0 6px 18px rgba(0,0,0,0.18);
    position: relative;
  }
  /* Front */
  .card--front .photo-panel {
    position: absolute;
    left: 20px; right: 20px; top: 20px;
    height: 214px;
    background: var(--white);
    display: flex; align-items: center; justify-content: center;
  }
  .card--front .photo {
    width: 420px; height: 176px;
    background: linear-gradient(90deg, #c9b59c 0%, #2b2724 45%, #2b2724 55%, #d4c2a9 100%);
    border-radius: 40px;
    opacity: 0.9;
  }
  .card--front .info {
    position: absolute;
    left: 20px; right: 20px; top: 246px;
    text-align: center;
  }
  .business-name {
    color: var(--white);
    font-weight: 700;
    font-size: 34px;
    letter-spacing: 0.5px;
    line-height: 1.05;
  }
  .contact-line {
    margin-top: 8px;
    color: var(--ink-soft);
    font-size: 15px;
    white-space: nowrap;
  }
  .website {
    margin-top: 4px;
    color: var(--ink);
    font-size: 16px;
    font-weight: 700;
  }
  /* Back */
  .card--back .inner {
    position: absolute;
    inset: 16px;
    background: var(--white);
    display: flex; flex-direction: column; align-items: center;
  }
  .tagline {
    margin-top: 26px;
    color: var(--taupe-text);
    font-weight: 700;
    font-style: italic;
    font-size: 26px;
  }
  .card--back .photo {
    margin-top: 26px;
    width: 380px; height: 210px;
    border-radius: 30px;
    background: radial-gradient(ellipse at 55% 45%, #b8794a 0%, #d9b99a 40%, #efe6dc 75%, #ffffff 100%);
  }
</style>
</head>
<body>
  <section class="card card--front">
    <div class="photo-panel">
      <div class="photo" role="img" aria-label="Three French bulldog puppies, two fawn and one black, sitting in a row"></div>
    </div>
    <div class="info">
      <h1 class="business-name">Merrywell Kennels</h1>
      <p class="contact-line">phone (555) 417-2983 • themerrywellkennel@examplemail.com</p>
      <p class="website">www.merrywellkennels-example.com</p>
    </div>
  </section>

  <section class="card card--back">
    <div class="inner">
      <p class="tagline">Quality pets and champion show dogs</p>
      <div class="photo" role="img" aria-label="English bulldog puppy resting over a patterned food bowl with spilled kibble"></div>
    </div>
  </section>
</body>
</html>
```